Brambleford Ponds Trifold About Us Leaflet

I need a A4 Trifold Leaflet Double sided designed with the following information on it:
Logo
Awards
Pictures - Please find on our website www.bramblefordponds.example.co.uk or www.social.example/bramblefordponds
Contact Information
Welcome Text
Events
Ideal for Text
Fishing Text
Camping Text
Map

This is almost a paper version of our website.

```html
<!DOCTYPE html>
<html lang="en">
<head>
<meta charset="utf-8">
<title>Brambleford Ponds – Trifold Leaflet</title>
<link href="https://fonts.googleapis.com/css2?family=Lato:wght@400;700;900&family=Amatic+SC:wght@700&display=swap" rel="stylesheet">
<style>
  :root{
    --stage:#e4e4e4;
    --white:#ffffff;
    --ink:#2b2b2b;
    --grey:#6b6b6b;
    --band-grey:#7d7d80;
    --orange:#f39a13;
    --green:#7cba2a;
    --green-dark:#5e9a1c;
    --lime:#b6e33a;
    --blue:#2a9ad8;
    --blue-dark:#1c6fb0;
    --events-blue:#1f84c6;
  }
  *{box-sizing:border-box;margin:0;padding:0}
  html,body{width:1200px;height:907px;overflow:hidden;background:var(--stage)}
  body{font-family:'Lato',sans-serif;color:var(--ink);position:relative}
  .leaflet{
    position:absolute;left:40px;top:55px;width:896px;height:638px;
    transform:scale(1.25);transform-origin:0 0;background:var(--white);
    box-shadow:0 4px 14px rgba(0,0,0,.25);overflow:hidden;
  }
  .leaflet__art{position:absolute;inset:0;width:896px;height:638px}
  .abs{position:absolute}

  /* inside panel: fishing */
  .section-tag{left:0;top:254px;width:85px;height:24px;background:var(--green);color:var(--white);
    font-weight:900;font-size:14px;line-height:24px;padding-left:14px;border-radius:0 12px 12px 0}
  .fishing-text{left:16px;top:292px;width:242px;font-size:11.6px;line-height:16.3px;text-align:justify;hyphens:auto;color:#333}
  .price-pill{left:0;top:505px;width:277px;height:53px;background:var(--orange);border-radius:0 27px 27px 0;
    color:var(--white);font-weight:900;font-size:16.5px;line-height:22px;padding:4px 0 0 16px}
  .price-pill span{font-weight:700}

  /* middle panel: events */
  .events-title{left:368px;top:316px;width:160px;height:40px;background:var(--white);border-radius:20px;
    color:var(--events-blue);font-weight:900;font-size:25px;line-height:40px;text-align:center;letter-spacing:.5px;
    box-shadow:0 3px 5px rgba(0,0,0,.2)}
  .events-list{left:310px;top:374px;width:276px;list-style:none;text-align:center;color:var(--white);
    font-weight:700;font-size:16.5px;line-height:22.7px}
  .events-list em{font-style:normal;color:var(--lime)}
  .contact-list{left:310px;top:490px;width:276px;list-style:none;text-align:center;color:var(--white);
    font-weight:700;font-size:12.5px;line-height:18px}
  .contact-list svg{width:9px;height:9px;vertical-align:-1px;margin-right:3px;fill:var(--lime)}

  /* cover panel */
  .brand{left:640px;top:24px;width:240px;text-align:center}
  .brand__name{font-weight:700;font-size:23px;color:var(--grey);display:inline-flex;align-items:center;gap:7px}
  .brand__name i{display:inline-block;width:12px;height:12px;border-radius:50%;background:var(--blue)}
  .brand__meta{margin-top:8px;display:flex;justify-content:space-between;font-size:7px;color:var(--grey);padding:0 6px}
  .brand__meta b{color:var(--green-dark)}
  .cover-title{left:600px;top:470px;width:296px;text-align:center;font-family:'Amatic SC',cursive;font-weight:700;
    font-size:45px;color:var(--white);letter-spacing:1px;line-height:50px}
  .cover-sub{left:600px;top:528px;width:296px;text-align:center;font-size:15px;color:#222;letter-spacing:.3px}
  .cover-phone{left:630px;top:571px;width:230px;height:37px;background:var(--white);border-radius:19px;
    text-align:center;font-weight:700;font-size:24px;line-height:37px;color:#222;box-shadow:0 3px 5px rgba(0,0,0,.2)}
</style>
</head>
<body>
<main class="leaflet">
  <svg class="leaflet__art" viewBox="0 0 896 638" aria-hidden="false">
    <defs>
      <clipPath id="panelLeft"><rect x="0" y="0" width="302" height="638"/></clipPath>
      <clipPath id="panelMid"><rect x="302" y="0" width="293" height="638"/></clipPath>
      <clipPath id="panelRight"><rect x="595" y="0" width="301" height="638"/></clipPath>
      <linearGradient id="kingfisherTone" x1="0" y1="0" x2="1" y2="1">
        <stop offset="0" stop-color="#3f6d2a"/><stop offset=".6" stop-color="#7da04a"/><stop offset="1" stop-color="#8a7e6a"/>
      </linearGradient>
      <linearGradient id="nightTone" x1="0" y1="0" x2="0" y2="1">
        <stop offset="0" stop-color="#1c2a3a"/><stop offset=".55" stop-color="#3b3826"/><stop offset="1" stop-color="#141a10"/>
      </linearGradient>
      <linearGradient id="blueFill" x1="0" y1="0" x2="1" y2="0">
        <stop offset="0" stop-color="var(--blue-dark)"/><stop offset=".5" stop-color="#2ea3e0"/><stop offset="1" stop-color="var(--blue-dark)"/>
      </linearGradient>
      <linearGradient id="anglerTone" x1="0" y1="0" x2="0" y2="1">
        <stop offset="0" stop-color="#6f8a4a"/><stop offset=".6" stop-color="#4e5e44"/><stop offset="1" stop-color="#8a8650"/>
      </linearGradient>
      <linearGradient id="greenFill" x1="0" y1="0" x2="0" y2="1">
        <stop offset="0" stop-color="#86c22e"/><stop offset="1" stop-color="#5f9a1b"/>
      </linearGradient>
      <radialGradient id="portraitTone"><stop offset="0" stop-color="#9a8a6a"/><stop offset="1" stop-color="#5f7a4a"/></radialGradient>
    </defs>

    <!-- inside left panel -->
    <g clip-path="url(#panelLeft)">
      <rect x="0" y="0" width="302" height="260" fill="url(#kingfisherTone)" role="img" aria-label="Photo of a kingfisher perched on a wooden post by the water"/>
      <path d="M0,68 C120,140 220,228 330,240 L330,638 L0,638 Z" fill="var(--white)"/>
      <path d="M0,30 C120,110 220,200 330,222 L330,240 C220,228 120,140 0,68 Z" fill="var(--white)"/>
      <path d="M0,48 C120,126 220,214 330,228 L330,236 C220,226 120,142 0,62 Z" fill="var(--band-grey)"/>
      <path d="M0,66 C120,146 220,234 330,244 L330,252 C220,246 120,162 0,86 Z" fill="var(--orange)"/>
    </g>
    <g>
      <circle cx="98" cy="168" r="66" fill="var(--green)"/>
      <circle cx="98" cy="168" r="60" fill="var(--white)"/>
      <circle cx="98" cy="168" r="57" fill="url(#portraitTone)" role="img" aria-label="Photo of an angler holding a carp by the lake"/>
    </g>

    <!-- inside middle panel -->
    <g clip-path="url(#panelMid)">
      <rect x="302" y="0" width="293" height="260" fill="url(#nightTone)" role="img" aria-label="Night photo of a camper van and lit tent on the pitch"/>
      <path d="M250,230 C300,234 340,242 380,242 C460,240 540,200 640,175 L640,638 L250,638 Z" fill="url(#blueFill)"/>
      <path d="M250,214 C300,222 340,228 380,228 C460,226 540,186 640,160 L640,176 C540,200 460,240 380,242 C340,242 300,234 250,230 Z" fill="var(--band-grey)"/>
      <path d="M250,230 C300,236 340,246 380,246 C460,244 540,204 640,180 L640,186 C540,210 460,250 380,250 C340,250 300,240 250,236 Z" fill="var(--white)"/>
    </g>

    <!-- cover panel -->
    <g clip-path="url(#panelRight)">
      <rect x="595" y="0" width="301" height="638" fill="url(#greenFill)"/>
      <path d="M595,0 L896,0 L896,140 C820,130 700,150 595,176 Z" fill="var(--white)"/>
      <path d="M595,190 C700,168 800,150 896,156 L896,430 C800,438 700,420 640,360 C615,330 600,290 595,250 Z" fill="url(#anglerTone)" role="img" aria-label="Photo of an angler kneeling on the bank holding a large carp"/>
      <path d="M595,176 C700,150 820,130 896,124 L896,140 C800,140 700,160 595,190 Z" fill="var(--band-grey)"/>
      <path d="M720,152 C790,138 850,130 896,128 L896,118 C850,118 790,128 720,152 Z" fill="var(--orange)"/>
      <path d="M595,250 C600,290 615,330 640,360 C700,420 800,438 896,430 L896,440 C800,448 700,430 636,370 C610,340 597,300 595,260 Z" fill="var(--white)"/>
      <path d="M595,262 C597,302 610,342 636,372 C700,432 800,450 896,442 L896,452 C800,462 700,442 630,380 C606,350 596,310 595,276 Z" fill="var(--orange)"/>
      <path d="M595,278 C596,312 606,352 630,382 C700,444 800,464 896,454 L896,462 C800,474 700,454 626,390 C603,360 596,322 595,292 Z" fill="var(--blue)"/>
    </g>

    <!-- bottom wave across inside panels -->
    <path d="M0,585 C120,560 300,560 420,580 C500,594 560,620 595,638 L0,638 Z" fill="var(--orange)"/>
    <path d="M0,592 C120,568 300,568 420,588 C500,602 560,626 595,642 L0,642 Z" fill="var(--green)"/>
    <path d="M0,598 C120,576 300,576 420,596 C500,610 560,630 590,642 L0,642 Z" fill="url(#greenFill)"/>
  </svg>

  <!-- inside left: fishing -->
  <div class="abs section-tag">FISHING</div>
  <p class="abs fishing-text">Brambleford Ponds is one of Somerset’s best kept secrets for decades, it is surrounded and hidden by a variety of indigenous trees and wildlife. It is an ideal place for a spot of fishing or just watching the wildlife. Brambleford Ponds are 4 acres, stocked with a selection of course fish including carp, bream, tench and others. Ranging to 25lbs We like to be different, we don’t offer pegs to fish from, you can fish anywhere on the bank. There is an onsite toilet and depending on the weather you can drive right to the bankside to save you carrying your fishing gear.</p>
  <div class="abs price-pill">£7 <span>per person per day (2 rods)</span><br>£5 <span>per half day</span></div>

  <!-- inside middle: events -->
  <h2 class="abs events-title">EVENTS</h2>
  <ul class="abs events-list">
    <li>Hayfield Scythe Fair <em>12th June</em></li>
    <li>Levels Country Games <em>31st July</em></li>
    <li>Music by the Ponds <em>13th Aug</em></li>
    <li>Family Fun Day <em>27th Aug</em></li>
  </ul>
  <ul class="abs contact-list">
    <li><svg viewBox="0 0 10 10"><path d="M2 0.5 L3.6 2.6 L2.7 3.6 C3.3 5 5 6.7 6.4 7.3 L7.4 6.4 L9.5 8 L8.4 9.5 C4.5 9.3 0.7 5.5 0.5 1.6 Z"/></svg>07700 900123</li>
    <li><svg viewBox="0 0 10 10"><path d="M0 2 H10 V8 H0 Z M0 2 L5 5.5 L10 2" stroke="#1f84c6" stroke-width=".8"/></svg>info@bramblefordponds.example.co.uk</li>
    <li><svg viewBox="0 0 10 10"><circle cx="5" cy="5" r="4.5"/></svg>www.bramblefordponds.example.co.uk</li>
  </ul>

  <!-- cover -->
  <div class="abs brand">
    <div class="brand__name"><i></i>Brambleford Ponds</div>
    <div class="brand__meta"><span>Ashcombe • Wellmead</span><span>Somerset • ZZ1 0AA<br><b>Tel: 01632 960811</b></span></div>
  </div>
  <h1 class="abs cover-title">BRAMBLEFORD PONDS</h1>
  <p class="abs cover-sub">CARAVAN AND CAMPING PARK</p>
  <div class="abs cover-phone">01632 960811</div>
</main>
</body>
</html>
```